Design of a chocolate packaging

In hand-lettering-style: "Thank you for your work - you are an important part of our team!" (in big letters - almost 2/3 of the whole place) "This chocolate is a lot, so you enter into a raffle and have a great chance of a Velora Kip and many more great winnings ... all the information is below www.tvk-sonnenkreis.de! Good luck !!! " (in small letters underneath) The place is: 7,3cm * 15,3cm (crosswise)

Script

```html
<!DOCTYPE html>
<html lang="de">
<head>
<meta charset="utf-8">
<title>Schokoladenverpackung – Danke</title>
<link rel="stylesheet" href="https://fonts.googleapis.com/css2?family=Delius+Unicase:wght@400;700&family=Open+Sans:wght@400;600&display=swap">
<style>
  :root {
    --bg: #ccd6d5;
    --wrapper-green: #86c08f;
    --gold: #eed98c;
    --ink: #141414;
    --url-gold: #d8b64a;
  }
  * { margin: 0; padding: 0; box-sizing: border-box; }
  html, body { width: 1200px; height: 1000px; overflow: hidden; background: var(--bg); }
  .canvas { position: relative; width: 1200px; height: 1000px; }
  .dieline {
    position: absolute; left: 165px; top: 30px;
    width: 725px; height: 783px;
    transform: scale(1.2); transform-origin: 0 0;
  }
  .dieline svg { position: absolute; inset: 0; }
  .front-panel { position: absolute; left: 0; top: 55px; width: 348px; height: 673px; }
  .line {
    position: absolute; right: 22px;
    font-family: "Delius Unicase", cursive;
    color: var(--ink); line-height: 1; white-space: nowrap;
  }
  .gold { color: var(--gold); font-weight: 700; text-shadow: -2px 2px 0 var(--ink); }
  .thanks { top: 22px; font-size: 56px; letter-spacing: 1px; }
  .tiny { font-size: 11px; }
  .for { top: 106px; }
  .mid { font-size: 34px; font-weight: 700; }
  .your { top: 118px; }
  .work { top: 156px; }
  .you-row { top: 210px; display: flex; align-items: flex-end; gap: 4px; }
  .you { font-size: 96px; }
  .are { font-size: 20px; font-weight: 700; color: var(--ink); text-shadow: none; margin-bottom: 4px; }
  .an { top: 330px; }
  .important { top: 342px; }
  .part { top: 385px; }
  .our { top: 445px; }
  .team { top: 457px; }
  .raffle-note {
    position: absolute; left: 0; width: 348px; top: 555px;
    text-align: center; font-family: "Open Sans", sans-serif;
    font-size: 9.2px; line-height: 12.4px; color: var(--ink);
  }
  .raffle-note .url { color: var(--url-gold); }
</style>
</head>
<body>
<main class="canvas">
  <section class="dieline">
    <svg viewBox="0 0 725 783" width="725" height="783" aria-hidden="true">
      <path fill="var(--wrapper-green)" d="M28 55 L28 10 L38 0 L338 0 L348 10 L348 55 L698 55 L725 82 L725 701 L698 728 L348 728 L348 773 L338 783 L38 783 L28 773 L28 728 L0 728 L0 55 Z"/>
    </svg>
    <div class="front-panel">
      <div class="line gold thanks">Danke</div>
      <div class="line tiny for">für</div>
      <div class="line mid your">Deine</div>
      <div class="line mid work">Arbeit</div>
      <div class="line gold you-row"><span class="you">Du</span><span class="are">bist</span></div>
      <div class="line tiny an">ein</div>
      <div class="line mid important">wichtiger</div>
      <div class="line mid part">Teil</div>
      <div class="line tiny our">unseres</div>
      <div class="line mid team">Teams!</div>
      <p class="raffle-note">
        Diese Schokolade ist ein Los.<br>
        Du nimmst damit an einer Verlosung Teil<br>
        und hast großartige Chancen<br>
        auf einen Velora Kip und viele weitere tolle Gewinne...<br>
        alle Infos gibt es unter<br>
        <span class="url">www.tvk-sonnenkreis.de</span><br>
        Viel Glück!!!
      </p>
    </div>
  </section>
</main>
</body>
</html>
```